We need a flyer, which gives an interested person an overview of our "product range". We offer perfomance testing (Leistungsdiagnostik), Personal-Training (the same in German), Strength Training (Athletiktraining), planning individual trainings (Trainingsplanung), company fitness (Firmenbetreuung), swim training (Schwimmtraining). There should also be our contact datas on it:
KVR - Kinetic Vantage Regime
Lindenweg 18
2517 Haberndorf
+43 676 83 21 054
office@kinvantregime.at
www.kinvantregime.at

If you need fotos for the flyer, you will find a lot of my facebookpage https://www.facebook.com/kineticvantageregime/?ref=bookmarks

NEW FOTOS ON THE FACEBOOKSITE!!!

Target Market(s)

companies, beginners, advanced, runners, triathletes,

Industry/Entity Type

Business

Requirements
Must have
• The Text should be in german words (in brackets).

```html
<!DOCTYPE html>
<html lang="de">
<head>
<meta charset="utf-8">
<title>KVR - Kinetic Vantage Regime – Flyer</title>
<link rel="stylesheet" href="https://fonts.googleapis.com/css2?family=Bebas+Neue&family=Open+Sans:wght@400;700&display=swap">
<style>
  :root {
    --white: #ffffff;
    --navy: #152a66;
    --sky: #0a9ddc;
    --sky-deep: #0088c9;
    --slate: #333c44;
    --text-light: #ffffff;
  }
  * { box-sizing: border-box; margin: 0; padding: 0; }
  html, body { width: 924px; height: 1200px; overflow: hidden; background: var(--white); }
  .flyer { position: relative; width: 924px; height: 1200px; overflow: hidden; background: var(--white); }
  .flyer__shapes { position: absolute; inset: 0; width: 924px; height: 1200px; }

  .brand { position: absolute; left: 80px; top: 104px; width: 224px; color: var(--navy);
    font-family: "Open Sans", sans-serif; font-weight: 700; text-align: center; }
  .brand__mark { font-size: 60px; line-height: 1; letter-spacing: 2px; }
  .brand__name { font-size: 15px; line-height: 1.2; margin-top: 6px; letter-spacing: 0.5px; }

  .services { font-family: "Bebas Neue", sans-serif; color: var(--text-light); font-size: 24px; letter-spacing: 0.3px; }
  .service, .service-dot { position: absolute; line-height: 1; }
  .service-dot { width: 7px; height: 7px; border-radius: 50%; background: var(--text-light); }

  .contact { font-family: "Open Sans", sans-serif; color: var(--text-light); font-size: 16px; line-height: 20px; }
  .contact__block { position: absolute; text-align: center; }
  .contact__divider { position: absolute; top: 1061px; width: 1.5px; height: 76px; background: var(--text-light); }
  .contact__brand { position: absolute; left: 62px; top: 1080px; width: 126px; text-align: center;
    font-family: "Open Sans", sans-serif; font-weight: 700; color: var(--text-light); }
  .contact__brand-mark { font-size: 28px; line-height: 1; letter-spacing: 1px; }
  .contact__brand-name { font-size: 9px; line-height: 1.2; margin-top: 3px; }
</style>
</head>
<body>
<main class="flyer">
  <svg class="flyer__shapes" viewBox="100 83 955 1351" preserveAspectRatio="none" xmlns="http://www.w3.org/2000/svg">
    <defs>
      <clipPath id="liftClip"><polygon points="620,83 1055,83 1055,1370 700,1040 470,839"/></clipPath>
      <clipPath id="benchClip"><polygon points="100,515 700,1040 100,1040"/></clipPath>
      <linearGradient id="liftBase" x1="0" y1="0" x2="1" y2="1">
        <stop offset="0" stop-color="#3b302c"/>
        <stop offset="0.5" stop-color="#6e4c3c"/>
        <stop offset="1" stop-color="#5a4438"/>
      </linearGradient>
      <radialGradient id="liftMetal" cx="0.5" cy="0.5" r="0.5">
        <stop offset="0" stop-color="#b4b0aa"/>
        <stop offset="0.55" stop-color="#7d7a76" stop-opacity="0.85"/>
        <stop offset="1" stop-color="#4a4644" stop-opacity="0"/>
      </radialGradient>
      <radialGradient id="liftSkin" cx="0.5" cy="0.5" r="0.5">
        <stop offset="0" stop-color="#c98a62"/>
        <stop offset="0.6" stop-color="#9a5e40" stop-opacity="0.8"/>
        <stop offset="1" stop-color="#7a4a34" stop-opacity="0"/>
      </radialGradient>
      <radialGradient id="liftShade" cx="0.5" cy="0.5" r="0.5">
        <stop offset="0" stop-color="#2a2220" stop-opacity="0.9"/>
        <stop offset="1" stop-color="#2a2220" stop-opacity="0"/>
      </radialGradient>
      <radialGradient id="liftWall" cx="0.5" cy="0.5" r="0.5">
        <stop offset="0" stop-color="#8c6a56"/>
        <stop offset="1" stop-color="#8c6a56" stop-opacity="0"/>
      </radialGradient>
      <linearGradient id="benchBase" x1="0" y1="0" x2="1" y2="1">
        <stop offset="0" stop-color="#e4e5e7"/>
        <stop offset="0.55" stop-color="#8d8580"/>
        <stop offset="1" stop-color="#1a1a1e"/>
      </linearGradient>
      <radialGradient id="benchNavy" cx="0.5" cy="0.5" r="0.5">
        <stop offset="0" stop-color="#1e3388"/>
        <stop offset="1" stop-color="#1e3388" stop-opacity="0"/>
      </radialGradient>
      <radialGradient id="benchSkin" cx="0.5" cy="0.5" r="0.5">
        <stop offset="0" stop-color="#c48e6e"/>
        <stop offset="1" stop-color="#c48e6e" stop-opacity="0"/>
      </radialGradient>
      <radialGradient id="benchDark" cx="0.5" cy="0.5" r="0.5">
        <stop offset="0" stop-color="#151518"/>
        <stop offset="1" stop-color="#151518" stop-opacity="0"/>
      </radialGradient>
      <linearGradient id="footerPanel" x1="0" y1="0" x2="0" y2="1">
        <stop offset="0" stop-color="#0a9ddc"/>
        <stop offset="1" stop-color="#0090d0"/>
      </linearGradient>
    </defs>

    <g role="img" aria-label="Photo: woman pressing a dumbbell at shoulder height in the gym" clip-path="url(#liftClip)">
      <rect x="460" y="83" width="600" height="1300" fill="url(#liftBase)"/>
      <ellipse cx="720" cy="150" rx="260" ry="160" fill="url(#liftShade)"/>
      <ellipse cx="890" cy="420" rx="240" ry="280" fill="url(#liftMetal)"/>
      <ellipse cx="560" cy="700" rx="150" ry="200" fill="url(#liftMetal)" opacity="0.7"/>
      <ellipse cx="660" cy="560" rx="170" ry="230" fill="url(#liftSkin)"/>
      <ellipse cx="800" cy="880" rx="220" ry="220" fill="url(#liftSkin)"/>
      <ellipse cx="1000" cy="1150" rx="180" ry="260" fill="url(#liftWall)" opacity="0.8"/>
    </g>
    <polygon class="accent-slate" points="620,83 470,839 345,729" fill="var(--slate)"/>
    <polygon class="accent-sky" points="620,83 345,729 245,642" fill="var(--sky)"/>
    <polygon class="accent-corner" points="100,485 132,513 100,515" fill="var(--sky-deep)"/>

    <g role="img" aria-label="Photo: woman doing a bench press with a trainer spotting the bar" clip-path="url(#benchClip)">
      <rect x="100" y="515" width="600" height="525" fill="url(#benchBase)"/>
      <ellipse cx="200" cy="740" rx="110" ry="100" fill="url(#benchSkin)" opacity="0.85"/>
      <ellipse cx="300" cy="930" rx="70" ry="100" fill="url(#benchSkin)" opacity="0.7"/>
      <ellipse cx="470" cy="880" rx="170" ry="120" fill="url(#benchNavy)"/>
      <ellipse cx="180" cy="880" rx="140" ry="90" fill="url(#benchDark)" opacity="0.8"/>
      <ellipse cx="560" cy="1010" rx="200" ry="60" fill="url(#benchDark)"/>
    </g>
    <polygon class="footer-panel" points="100,1040 700,1040 1055,1370 1055,1434 100,1434" fill="url(#footerPanel)"/>
  </svg>

  <header class="brand">
    <div class="brand__mark">KVR</div>
    <div class="brand__name">Kinetic Vantage Regime</div>
  </header>

  <section class="services" aria-label="Leistungen">
    <span class="service" style="left:117px; top:919px;">Athletiktraining</span>
    <span class="service-dot" style="left:270px; top:927px;"></span>
    <span class="service" style="left:309px; top:919px;">Trainingsplanung</span>
    <span class="service-dot" style="left:474px; top:927px;"></span>
    <span class="service" style="left:504px; top:919px;">Schwimmtraining</span>

    <span class="service" style="left:74px; top:985px;">Leistungsdiagnostik</span>
    <span class="service-dot" style="left:261px; top:993px;"></span>
    <span class="service" style="left:308px; top:985px;">Personal-Training</span>
    <span class="service-dot" style="left:478px; top:993px;"></span>
    <span class="service" style="left:529px; top:985px;">Firmenbetreuung</span>
  </section>

  <footer class="contact">
    <div class="contact__brand">
      <div class="contact__brand-mark">KVR</div>
      <div class="contact__brand-name">Kinetic Vantage Regime</div>
    </div>
    <span class="contact__divider" style="left:198px;"></span>
    <div class="contact__block" style="left:200px; width:178px; top:1081px;">KVR - Kinetic<br>Vantage Regime</div>
    <span class="contact__divider" style="left:379px;"></span>
    <div class="contact__block" style="left:381px; width:186px; top:1070px;">Lindenweg 18<br>2517 Haberndorf<br>+43 676 83 21 054</div>
    <span class="contact__divider" style="left:567px;"></span>
    <div class="contact__block" style="left:570px; width:270px; top:1082px;">office@kinvantregime.at<br>www.kinvantregime.at</div>
  </footer>
</main>
</body>
</html>
```